Spa Business Card Design Project

Hello! We are a boutique spa for men and women that is rebranding. I would like a memorable new business card that showcases our beautiful new logo and our unique business. I would like it to be classic/timeless and eclectic/artistic at the  same time.
I am a fan of negative space as you can tell from the logo. I am also open to any creative ideas.
Multi sided design. Two sided design is acceptable as an option, too. "Flaps/folds/whatever the design term is" are optional- whether full vertical or horizontal, half flap, full flap etc
On either side next to the golden snail I would potentially like to see "Ease up. Savor the Day."  Possibly on one statment on top of each other, crowned with the snail. Or the statment following the snail on one line... I am open for a creative suprise, too.
The back I would like room for the standard Information
"3817 Birch Lane
Alderbrook, Vermont 05731
(802) 462 3085
info@thecorvella spa.com
The snail is to be done in gold ink.
Can I also Have an option for cards that are individualized for staff members, too?

Updates
Project Deadline Extended
Reason: I apologize for the deadline extension. My day was more involved than anticipated in other matters. Hope to have this closed by next Tuesday.
Thank you

Target Market(s)
Men and women with expendable income between the ages of 30-55
Industry/Entity Type
Boutique
Requirements
Must have
- only black and gold ink.

Nice to have
- One of a kind.
Showcase the snail :-)
make you smile :-)
Fun, but professional.
Should not have
- Lots of color.
Too feminine.
Too busy.

```html
<!DOCTYPE html>
<html lang="en">
<head>
<meta charset="utf-8">
<title>The Corvella Spa – Business Card</title>
<link href="https://fonts.googleapis.com/css2?family=Questrial&family=Arimo:wght@700&display=swap" rel="stylesheet">
<style>
  :root {
    --gold: #c9a052;
    --ink: #000000;
    --paper: #ffffff;
  }
  html, body {
    margin: 0;
    padding: 0;
    width: 1038px;
    height: 1200px;
    overflow: hidden;
    background: var(--paper);
  }
  .sheet { display: block; width: 1038px; height: 1200px; }
  .brand-name { font-family: "Questrial", sans-serif; font-size: 62px; letter-spacing: 1px; }
  .tagline { font-family: "Questrial", sans-serif; font-size: 16px; }
  .slogan { font-family: "Arimo", sans-serif; font-weight: 700; font-size: 40px; fill: var(--gold); }
  .person-name { font-family: "Questrial", sans-serif; font-size: 52px; fill: var(--ink); }
  .person-title { font-family: "Questrial", sans-serif; font-size: 30px; fill: var(--ink); }
  .contact { font-family: "Questrial", sans-serif; font-size: 26px; fill: var(--ink); }
  .fill-gold { fill: var(--gold); }
  .fill-ink { fill: var(--ink); }
  .frame-ink { fill: none; stroke: var(--ink); stroke-width: 4; }
  .frame-gold { fill: none; stroke: var(--gold); stroke-width: 4; }
</style>
</head>
<body>
<svg class="sheet" viewBox="0 0 1038 1200" xmlns="http://www.w3.org/2000/svg">
  <defs>
    <clipPath id="front-shape">
      <path d="M58,0 H1032 Q1038,0 1038,6 V468 A110,110 0 0 1 928,578 H6 Q0,578 0,572 V58 A58,58 0 0 1 58,0 Z"/>
    </clipPath>
    <clipPath id="back-shape">
      <path d="M6,0 H928 A110,110 0 0 1 1038,110 V572 Q1038,578 1032,578 H58 A58,58 0 0 1 0,520 V6 Q0,0 6,0 Z"/>
    </clipPath>
    <clipPath id="front-upper"><rect x="0" y="0" width="1038" height="274"/></clipPath>
    <clipPath id="front-lower"><rect x="0" y="274" width="1038" height="304"/></clipPath>
    <clipPath id="back-upper"><rect x="0" y="0" width="1038" height="275"/></clipPath>
    <clipPath id="back-lower"><rect x="0" y="275" width="1038" height="303"/></clipPath>
    <path id="slogan-curve" d="M64,392 Q330,480 670,414"/>
  </defs>

  <!-- Front of card -->
  <g class="card card-front">
    <g clip-path="url(#front-shape)">
      <rect class="fill-gold band-upper" x="0" y="0" width="1038" height="274"/>
      <rect class="fill-ink band-lower" x="0" y="274" width="1038" height="304"/>
    </g>
    <g class="card-frame">
      <path class="frame-ink" clip-path="url(#front-upper)" d="M18,18 H1018 V490 A70,70 0 0 1 948,560 H18 Z"/>
      <path class="frame-gold" clip-path="url(#front-lower)" d="M18,18 H1018 V490 A70,70 0 0 1 948,560 H18 Z"/>
    </g>
    <text class="brand-name fill-ink" x="519" y="176" text-anchor="middle">The Corvella Spa</text>
    <text class="tagline fill-ink" x="519" y="226" text-anchor="middle">a boutique spa for Men &amp; Women</text>
    <text class="slogan"><textPath href="#slogan-curve" textLength="600" lengthAdjust="spacing">Ease up. Savor the Day.</textPath></text>
    <rect class="fill-gold snail-illustration" role="img" aria-label="Gold snail illustration" x="686" y="228" width="280" height="196" rx="48"/>
  </g>

  <!-- Back of card -->
  <g class="card card-back" transform="translate(0,622)">
    <g clip-path="url(#back-shape)">
      <rect class="fill-ink band-upper" x="0" y="0" width="1038" height="275"/>
      <rect class="fill-gold band-lower" x="0" y="275" width="1038" height="303"/>
    </g>
    <g class="card-frame">
      <path class="frame-gold" clip-path="url(#back-upper)" d="M18,18 H948 A70,70 0 0 1 1018,88 V560 H18 Z"/>
      <path class="frame-ink" clip-path="url(#back-lower)" d="M18,18 H948 A70,70 0 0 1 1018,88 V560 H18 Z"/>
    </g>
    <text class="brand-name fill-gold" x="519" y="168" text-anchor="middle">The Corvella Spa</text>
    <text class="tagline fill-gold" x="519" y="228" text-anchor="middle">a boutique spa for Men &amp; Women</text>

    <text class="person-name" x="284" y="424" text-anchor="middle">Person Name</text>
    <text class="person-title" x="284" y="468" text-anchor="middle">Title</text>

    <g class="contact-block">
      <text class="contact" x="622" y="352">3817 Birch Lane</text>
      <text class="contact" x="622" y="387">Alderbrook, Vermont 05731</text>
      <text class="contact" x="622" y="450">(802) 462 3085</text>
      <text class="contact" x="622" y="516">info@thecorvella spa.com</text>
    </g>
  </g>
</svg>
</body>
</html>
```